Business Card Design Project

I need some business cards with the logo you did for us (attached)
I am looking for a coulourful yet serious business card

We do market research
on the back I want the logo

on the front my name : Corinne Valdessac
position : Manager
address : Brume Analytica Sarl - 27 Rue des tanneurs
1847 Glarency - Switzerland
corinne.valdessac@brumeanalytica.ch
Tel : +4122 934 07 58
Mob France :+33 671 42 8356
Mob Italy +39 347 520 8163

The tree of the logo could also be used alone

THE BACKGROUND COLOR ON THE FRONT HAS TO BE WHITE, ON THE BACK YU CAN TRY OHER COLOUR BUT HOMOGENEOUS (NOT EXPENSIVE TO PRINT)

Target Market(s)

multinational companies or other market research companies

Industry/Entity Type

Market Research

Requirements
Must have
• logo on the back
and all the info above

```html
<!DOCTYPE html>
<html lang="en">
<head>
<meta charset="utf-8">
<title>Brume Analytica – Business Card</title>
<link rel="stylesheet" href="https://fonts.googleapis.com/css2?family=Didact+Gothic&display=swap">
<style>
  :root {
    --backdrop: #e9e7e4;
    --card: #ffffff;
    --magenta-band: #e2117a;
    --crimson-band: #a10203;
    --brand-text: #d8166f;
    --body-text: #1e1e1e;
    --dot-lime: #8fd61e;
    --dot-amber: #fdb813;
    --dot-fuchsia: #e514d2;
    --mark-soft-a: #fbe3a6;
    --mark-soft-b: #f7c6e2;
    --mark-soft-c: #d6f2b0;
  }
  * { margin: 0; padding: 0; box-sizing: border-box; }
  html, body {
    width: 826px; height: 1200px; overflow: hidden;
    background: var(--backdrop);
    font-family: "Didact Gothic", "Century Gothic", sans-serif;
  }
  .canvas { position: relative; width: 826px; height: 1200px; }

  .card { position: absolute; background: var(--card); box-shadow: 0 2px 6px rgba(0,0,0,.18); }

  /* back of card */
  .card-back { left: 215px; top: 44px; width: 374px; height: 674px; }
  .brand-symbol {
    position: absolute; left: 12px; top: 40px;
    width: 350px; height: 350px; border-radius: 50%;
    background: linear-gradient(160deg, var(--mark-soft-a) 0%, var(--mark-soft-b) 55%, var(--mark-soft-c) 100%);
  }
  .brand-mark {
    position: absolute; right: 16px; top: 528px;
    text-align: right; color: var(--brand-text);
    font-size: 38px; line-height: 40px; letter-spacing: -0.5px;
  }

  /* front of card */
  .card-front { left: 91px; top: 744px; width: 674px; height: 374px; }
  .name-band {
    position: absolute; left: 0; top: 26px; width: 100%; height: 52px;
    background: var(--magenta-band); color: #fff;
    font-size: 29px; line-height: 52px; text-align: center;
  }
  .role-band {
    position: absolute; left: 0; top: 78px; width: 100%; height: 32px;
    background: var(--crimson-band); color: #fff;
    font-size: 21px; line-height: 32px; text-align: center; letter-spacing: 1px;
  }
  .contact-row { position: absolute; left: 20px; display: flex; align-items: center; }
  .contact-row .dot { width: 40px; flex: none; }
  .contact-text {
    margin-left: 22px; color: var(--body-text);
    font-size: 23px; line-height: 31px; white-space: nowrap;
  }
  .row-email { top: 122px; }
  .row-phone { top: 171px; }
  .row-address { top: 289px; }
</style>
</head>
<body>
<main class="canvas">

  <section class="card card-back" aria-label="Back of card">
    <div class="brand-symbol" role="img" aria-label="Brand tree symbol area"></div>
    <div class="brand-mark">brume<br>analytica</div>
  </section>

  <section class="card card-front" aria-label="Front of card">
    <div class="name-band">Corinne Valdessac</div>
    <div class="role-band">MANAGER</div>

    <div class="contact-row row-email">
      <svg class="dot" width="40" height="40" viewBox="0 0 40 40"><circle cx="20" cy="20" r="18" fill="var(--dot-lime)"/></svg>
      <p class="contact-text">corinne.valdessac@brumeanalytica.ch</p>
    </div>

    <div class="contact-row row-phone">
      <svg class="dot" width="40" height="40" viewBox="0 0 40 40"><circle cx="20" cy="20" r="18" fill="var(--dot-amber)"/></svg>
      <p class="contact-text">Tel : +4122 934 07 58<br>Mob France :+33 671 42 8356<br>Mob Italy +39 347 520 8163</p>
    </div>

    <div class="contact-row row-address">
      <svg class="dot" width="40" height="40" viewBox="0 0 40 40"><circle cx="20" cy="20" r="18" fill="var(--dot-fuchsia)"/></svg>
      <p class="contact-text">Brume Analytica Sarl - 27 Rue des tanneurs<br>1847 Glarency - Switzerland</p>
    </div>
  </section>

</main>
</body>
</html>
```